Homepage design for car dealership - JRW Auto (2908)

BANNER
Dealership Info
JRW Auto Brokers Inc (logo attached)
Phone 888-555-0147
Address 1127 Dovecote Lane, Alexandria, MN 56399
Tagline Your best vehicle value is as easy as J-R-W
Hours Mon-Fri: 9a – 6p
Sat: 9a – 3p
DESIGN & LAYOUT
Theme: Geographic
Background: collage, similar to Pinewood Auto Mart
Accent Colors: Earth tones, with a pop of yellow (match yellow in logo provided)
Featured Vehicles location: bottom
Social Networking: none
8 Slideshow Images
1. 2010-2012 Marlo Zephyrin
2. 2008-2012 Kovani Pickup
3. 2008-2012 Velt sedan
4. 2008-2012 Brax SUV
5. 2008-2012 Kovani sedan
6. 2008-2012 Marlo Pickup
7. 2008-2012 Montrell sedan
8. 2008-2012 Brax Pickup
Call-to-Action Buttons
Assured Loan Greenlight (find logo for Assured Loan Greenlight)
Warranty
About Us
Service
Specifications - a sample site psd has been attached for review for an idea of the size specifications. Feel free to change up the layout and make it unique.
Design Notes:
-In the collage background, the client wants to use mostly images of families (including their kids), and some images of Minnesota lakes and other scenery
-Open to the use of transparent or solid content background
-Logo provided by client doesn’t match the geographical theme, please do what you can with it, or use a similar font to design something that will blend in more with the theme.
SAMPLE SITES Client provided the following links to other websites whose design and colors he liked.
1. current site: www.jrwautobrokers-demo.info
2. liked: www.pinewoodautomart-demo.com
Target Market(s)
car buyers
Call

```html
<!DOCTYPE html>
<html lang="en">
<head>
<meta charset="utf-8">
<title>JRW Auto Brokers Inc</title>
<link href="https://fonts.googleapis.com/css2?family=Roboto:wght@300;400;500;700&display=swap" rel="stylesheet">
<style>
:root{
  --yellow:#f6d600;
  --yellow-dark:#d9b800;
  --ink:#222;
  --panel:#fff;
  --page:#efefef;
  --line:#d8d8d8;
  --footer:#252525;
}
*{box-sizing:border-box;margin:0;padding:0}
html,body{width:986px;height:1200px;overflow:hidden}
body{font-family:'Roboto',sans-serif;color:var(--ink);position:relative;
  background:linear-gradient(180deg,#8a9aa8 0%,#3b6f93 30%,#6b7f63 55%,#2f6a92 75%,#7b8b93 100%)}
.collage{position:absolute;inset:0}
.page{position:absolute;left:141px;top:0;width:704px;height:1200px;background:var(--page)}
.abs{position:absolute}
.brand{left:14px;top:28px;font-size:24px;font-weight:700;color:#111;letter-spacing:-.3px}
.brand-dot{display:inline-block;width:14px;height:14px;background:var(--yellow);margin-right:8px;vertical-align:middle}
.tagline{left:14px;top:94px;font-size:9.5px;color:#444}
.search{left:355px;top:14px;width:242px;height:24px;border:1px solid #ccc;background:#fff;font-size:9px;color:#aaa;padding:6px 7px}
.search-btn{left:604px;top:14px;width:87px;height:24px;background:var(--yellow);color:#222;font-size:12px;font-weight:500;text-align:center;line-height:22px;border:1px solid var(--yellow-dark)}
.info{font-size:10px;color:#333;display:flex;align-items:center;gap:6px;white-space:nowrap}
.info u{font-weight:500}
.ico{width:17px;height:17px;background:var(--yellow);display:inline-flex;align-items:center;justify-content:center;border-radius:2px}
.rule{left:354px;width:338px;height:1px;background:#ddd}
.nav{position:absolute;left:134px;top:118px;width:718px;height:39px;background:var(--yellow);display:flex;align-items:center;padding-left:21px}
.nav a{font-size:11.5px;color:#333;text-decoration:none;padding:0 28px;border-right:1px solid rgba(0,0,0,.15);line-height:22px}
.nav a:first-child{color:#fff;padding-left:5px}
.nav a:last-child{border:none}
.hero{left:14px;top:170px;width:676px;height:254px;background:linear-gradient(180deg,#6d6a64 0%,#9a8d74 45%,#5c5d5e 75%,#3e3f41 100%)}
.tabs{left:14px;top:452px;display:flex;gap:8px}
.tab{position:relative;height:25px;border:1px solid #ccc;background:#f6f6f6;font-size:11.5px;color:#333;text-align:center;line-height:23px;white-space:nowrap}
.tab.on{background:var(--yellow);color:#fff;border-color:var(--yellow-dark)}
.tab b{position:absolute;top:-8px;right:4px;width:14px;height:14px;border-radius:50%;background:#111;color:#fff;font-size:8px;line-height:14px;font-weight:400}
.panel{background:var(--panel);border:1px solid var(--line)}
.panel h2{font-size:18px;font-weight:500;color:#222;padding-bottom:4px;border-bottom:1px solid #ccc}
.contact{left:14px;top:491px;width:210px;height:250px;padding:12px 14px}
.field{height:20px;border:1px solid #ccc;margin-top:7px;font-size:8.5px;color:#aaa;padding:4px 6px}
.field:first-of-type{margin-top:14px}
.field.tall{height:41px}
.submit{position:absolute;right:14px;top:210px;width:82px;height:25px;background:var(--yellow);border:1px solid var(--yellow-dark);font-size:11.5px;font-weight:500;text-align:center;line-height:23px}
.welcome{left:238px;top:491px;width:453px;height:250px;padding:12px 14px}
.welcome p{font-size:9.2px;line-height:12.8px;color:#666;margin-top:12px}
.welcome p.lead{font-size:11px;line-height:13px;color:#111;margin-top:13px}
.credit{position:absolute;right:14px;top:208px;width:136px;height:27px;border:1px solid #555;display:flex}
.credit span:first-child{flex:1;font-size:8px;font-style:italic;color:#555;padding:3px 4px;line-height:9.5px}
.credit span:last-child{width:50px;background:#333;color:#fff;font-size:9px;font-weight:700;text-align:center;line-height:10px;padding-top:3px}
.featured{left:14px;top:754px;width:677px;height:311px;padding:10px 14px}
.thumb{position:absolute;width:97px;height:73px;border:1px solid #ddd}
.footer{left:0;top:1101px;width:704px;height:99px;background:var(--footer)}
.foot-links{position:absolute;top:12px;width:100%;text-align:center;font-size:9.5px;color:#888;white-space:nowrap}
.foot-links span{margin:0 7px}
.foot-rule{position:absolute;left:60px;right:60px;top:43px;height:1px;background:#3a3a3a}
.copy{position:absolute;top:54px;width:100%;text-align:center;font-size:9.5px;color:var(--yellow)}
</style>
</head>
<body>
<div class="collage" role="img" aria-label="Collage of family photos and lake scenery"></div>
<div class="page">
  <div class="abs brand"><span class="brand-dot"></span>JRW Auto Brokers Inc</div>
  <div class="abs tagline">Your best vehicle value is as easy as J-R-W</div>
  <div class="abs search">Enter Your Keyword</div>
  <div class="abs search-btn">Search</div>
  <div class="abs info" style="left:355px;top:52px">
    <span class="ico"><svg width="10" height="10" viewBox="0 0 10 10"><path d="M2 1h2l1 2-1 1c.6 1.2 1.5 2.1 2.7 2.7l1-1 2 1v2c0 .5-.5 1-1 1C4.5 9.7.3 5.5 1 2c0-.5.5-1 1-1z" fill="#222"/></svg></span>
    Phone # : <u>888-555-0147</u>
  </div>
  <div class="abs info" style="left:517px;top:52px">
    <span class="ico"><svg width="10" height="10" viewBox="0 0 10 10"><circle cx="5" cy="5.5" r="3.6" fill="none" stroke="#222" stroke-width="1.2"/><path d="M5 3.5v2h1.5" stroke="#222" fill="none"/></svg></span>
    Mon-Fri : <u>9a – 6p</u>&nbsp; Sat : <u>9a – 3p</u>
  </div>
  <div class="abs rule" style="top:77px"></div>
  <div class="abs info" style="left:396px;top:86px">
    <span class="ico"><svg width="10" height="10" viewBox="0 0 10 10"><path d="M5 9.5S1.8 6 1.8 4a3.2 3.2 0 0 1 6.4 0C8.2 6 5 9.5 5 9.5z" fill="none" stroke="#222" stroke-width="1.1"/><circle cx="5" cy="4" r="1.1" fill="#222"/></svg></span>
    Address :&nbsp; <span><u>1127</u> Dovecote Lane, Lakemere, NK <u>56399</u></span>
  </div>

  <div class="abs hero" role="img" aria-label="Silver wagon driving on a road, motion-blurred background"></div>
  <div class="abs tabs">
    <div class="tab" style="width:75px">Marlo<b>12</b></div>
    <div class="tab on" style="width:59px">Dalver<b>5</b></div>
    <div class="tab" style="width:49px">Brax<b>5</b></div>
    <div class="tab" style="width:68px">Crestline<b>4</b></div>
    <div class="tab" style="width:67px">Montrell<b>2</b></div>
    <div class="tab" style="width:50px">GRX<b>2</b></div>
    <div class="tab" style="width:54px">Bellamy<b>1</b></div>
    <div class="tab" style="width:68px">Hanwell<b>1</b></div>
    <div class="tab" style="width:42px">Kirra<b>1</b></div>
    <div class="tab" style="width:70px">Meridan<b>1</b></div>
  </div>
  <div class="abs panel contact">
    <h2>Contact Dealer</h2>
    <div class="field">First Name:</div>
    <div class="field">Last Name:</div>
    <div class="field">Phone:</div>
    <div class="field">E-Mail:</div>
    <div class="field tall">Comments.</div>
    <div class="submit">Submit</div>
  </div>
  <div class="abs panel welcome">
    <h2>Welcome</h2>
    <p>Welcome to JRW Auto Brokers, home of the best used cars in Lakemere, Northmark. We have worked hard to build a reputation for selling high quality used cars backed by extraordinary service. Most of our business is done with individuals who've never even driven the vehicle or seen it in person prior to purchasing. Only two things make that possible: unequaled quality and a high level of service.</p>
    <p>We offer a variety of car financing programs to meet the individual needs of our customers, and provide our customers with a variety of extended warranty plans to protect their used car after a purchase has been made.</p>
    <p class="lead">Please use the menu above to browse our current inventory and learn more about us. If you have any questions please feel free to call us at 888-555-0147.</p>
    <div class="credit"><span>Assured Loan Greenlight</span><span>APPLY<br>NOW!</span></div>
  </div>
  <div class="abs panel featured">
    <h2>Featured Vehicles</h2>
    <div class="thumb" style="left:14px;top:49px;background:linear-gradient(#d8d8d8,#b22 60%,#999)" role="img" aria-label="Red sedan"></div>
    <div class="thumb" style="left:124px;top:49px;background:linear-gradient(#aaa,#b33 55%,#777)" role="img" aria-label="Red sedan front view"></div>
    <div class="thumb" style="left:234px;top:49px;background:linear-gradient(#fff,#333 55%,#eee)" role="img" aria-label="Black SUV"></div>
    <div class="thumb" style="left:344px;top:49px;background:linear-gradient(#eee,#999 55%,#ddd)" role="img" aria-label="Silver pickup truck"></div>
    <div class="thumb" style="left:454px;top:49px;background:linear-gradient(#888,#555 55%,#777)" role="img" aria-label="Grey SUV"></div>
    <div class="thumb" style="left:564px;top:49px;background:linear-gradient(#eee,#e8e8e8 55%,#c9a040)" role="img" aria-label="White SUV"></div>
    <div class="thumb" style="left:14px;top:136px;background:linear-gradient(#f2f2f2,#bbb 55%,#eee)" role="img" aria-label="Silver hatchback"></div>
    <div class="thumb" style="left:124px;top:136px;background:linear-gradient(#ccc,#aaa 55%,#8a7c6a)" role="img" aria-label="Silver sedan"></div>
    <div class="thumb" style="left:234px;top:136px;background:linear-gradient(#5a7a4a,#b8c0c8 55%,#6a8a55)" role="img" aria-label="Silver sedan on grass"></div>
    <div class="thumb" style="left:344px;top:136px;background:linear-gradient(#8a8070,#aaa 55%,#777)" role="img" aria-label="Silver wagon"></div>
    <div class="thumb" style="left:454px;top:136px;background:linear-gradient(#6a8a50,#222 60%,#8a7a60)" role="img" aria-label="Black sedan"></div>
    <div class="thumb" style="left:564px;top:136px;background:linear-gradient(#c4501a,#9aa 55%,#c4501a)" role="img" aria-label="Orange sedan grille close-up"></div>
    <div class="thumb" style="left:14px;top:223px;background:linear-gradient(#eee,#555 55%,#ddd)" role="img" aria-label="Grey SUV"></div>
    <div class="thumb" style="left:124px;top:223px;background:linear-gradient(#f2f2f2,#bbb 55%,#eee)" role="img" aria-label="Silver hatchback"></div>
    <div class="thumb" style="left:234px;top:223px;background:linear-gradient(#fff,#333 55%,#eee)" role="img" aria-label="Black SUV"></div>
    <div class="thumb" style="left:344px;top:223px;background:linear-gradient(#aaa,#b33 55%,#777)" role="img" aria-label="Red sedan front view"></div>
    <div class="thumb" style="left:454px;top:223px;background:linear-gradient(#ccc,#aaa 55%,#8a7c6a)" role="img" aria-label="Silver sedan"></div>
    <div class="thumb" style="left:564px;top:223px;background:linear-gradient(#8a8070,#aaa 55%,#777)" role="img" aria-label="Silver wagon"></div>
  </div>
  <div class="abs footer">
    <div class="foot-links"><span>Home</span><span>Inventory</span><span>Vehicle Finder</span><span>Site Map</span><span>Contact Us</span><span>/</span><span>1127 Dovecote Lane, Lakemere, Northmark 56399 &nbsp;555.555.0188</span></div>
    <div class="foot-rule"></div>
    <div class="copy">Copyright © 2003-2014 DriveNova, LTD. All Rights Reserved.</div>
  </div>
</div>
<nav class="nav">
  <a>Home</a><a>Inventory</a><a>Vehicle Finder</a><a>About Us</a><a>Contact Us</a>
</nav>
</body>
</html>
```